Business Card Design Project for Investment Fund

Orvanel Asset Partners is an emerging wealth management firm based in New Jersey. It offers superior investment returns to high net worth individuals and institutions by finding undervalued assets.
We recently selected a company logo which was inspired by the Tucana constellation. Beta Tucanae is a group of six stars, containing star cluster 47 Tucanae, rated the second brightest object in the sky.
Now we need a business card design. Since we are an investment firm, the design should project a sense of stability, growth and professionalism. The owner is interested in something simple yet striking, which of course is consistent with the logo.
Target Market(s)
Wealthy individuals, probably middle aged or older, in the US
Industry/Entity Type
Investment

```html
<!DOCTYPE html>
<html lang="en">
<head>
<meta charset="utf-8">
<title>Orvanel Asset Partners — Business Card</title>
<link rel="stylesheet" href="https://fonts.googleapis.com/css2?family=Open+Sans:wght@400;600&family=Pinyon+Script&display=swap">
<style>
  :root {
    --page-bg: #e6e7ea;
    --card-bg: #ffffff;
    --ink: #2b2d33;
    --ink-soft: #4a4d55;
    --brand-navy: #2a2f9c;
    --signature-blue: #1f3fb8;
    --card-shadow: rgba(20, 22, 30, 0.18);
  }
  * { box-sizing: border-box; margin: 0; padding: 0; }
  html, body { width: 1200px; height: 800px; overflow: hidden; }
  body {
    background: var(--page-bg);
    font-family: "Open Sans", Arial, sans-serif;
    color: var(--ink);
    position: relative;
  }
  .card {
    position: absolute;
    width: 560px;
    height: 320px;
    background: var(--card-bg);
    box-shadow: 0 10px 28px var(--card-shadow);
  }
  .card--back { left: 560px; top: 60px; }
  .card--front { left: 80px; top: 400px; }

  .brand {
    position: absolute;
    display: flex;
    align-items: center;
    gap: 12px;
  }
  .brand__square {
    width: 46px;
    height: 46px;
    border-radius: 8px;
    background: var(--brand-navy);
    flex: none;
  }
  .brand__name {
    font-weight: 600;
    font-size: 19px;
    color: var(--ink);
    letter-spacing: 0.3px;
  }
  .card--back .brand { left: 50%; top: 108px; transform: translateX(-50%); }
  .card--back .website {
    position: absolute;
    left: 0; right: 0; top: 188px;
    text-align: center;
    font-size: 14px;
    color: var(--ink);
  }
  .card--front .brand { left: 44px; top: 50px; }

  .contact {
    position: absolute;
    right: 36px;
    bottom: 28px;
    text-align: right;
  }
  .contact__name {
    font-family: "Pinyon Script", cursive;
    font-size: 32px;
    color: var(--signature-blue);
    line-height: 1.1;
  }
  .contact__title {
    font-size: 15px;
    color: var(--ink);
    margin-bottom: 10px;
  }
  .contact__address {
    font-size: 14px;
    line-height: 1.35;
    margin-bottom: 10px;
    padding-right: 26px;
  }
  .contact__list { list-style: none; }
  .contact__item {
    display: flex;
    justify-content: flex-end;
    align-items: center;
    gap: 10px;
    font-size: 14px;
    line-height: 1.6;
  }
  .contact__icon {
    width: 16px;
    height: 16px;
    flex: none;
    color: var(--brand-navy);
  }
</style>
</head>
<body>
  <section class="card card--back" aria-label="Card back">
    <div class="brand">
      <span class="brand__square"></span>
      <span class="brand__name">Orvanel Asset Partners</span>
    </div>
    <p class="website">www.orvanelpartners.com</p>
  </section>

  <section class="card card--front" aria-label="Card front">
    <div class="brand">
      <span class="brand__square"></span>
      <span class="brand__name">Orvanel Asset Partners</span>
    </div>

    <div class="contact">
      <p class="contact__name">Corwin Hale</p>
      <p class="contact__title">CEO</p>
      <p class="contact__address">77 Halden St<br>Harbor City, NJ 07030</p>
      <ul class="contact__list">
        <li class="contact__item">
          <span>201-555-0143</span>
          <svg class="contact__icon" viewBox="0 0 16 16" aria-hidden="true">
            <rect x="4" y="1" width="8" height="14" rx="1.5" fill="none" stroke="currentColor" stroke-width="1.5"/>
            <rect x="5.5" y="3" width="5" height="6" fill="currentColor"/>
            <circle cx="8" cy="12.3" r="0.9" fill="currentColor"/>
          </svg>
        </li>
        <li class="contact__item">
          <span>chale@orvanelpartners.com</span>
          <svg class="contact__icon" viewBox="0 0 16 16" aria-hidden="true">
            <rect x="1.5" y="3.5" width="13" height="9" fill="none" stroke="currentColor" stroke-width="1.5"/>
            <path d="M1.5 3.5 L8 9 L14.5 3.5" fill="none" stroke="currentColor" stroke-width="1.5"/>
          </svg>
        </li>
        <li class="contact__item">
          <span>www.orvanelpartners.com</span>
          <svg class="contact__icon" viewBox="0 0 16 16" aria-hidden="true">
            <circle cx="8" cy="8" r="6.3" fill="none" stroke="currentColor" stroke-width="1.4"/>
            <ellipse cx="8" cy="8" rx="2.8" ry="6.3" fill="none" stroke="currentColor" stroke-width="1.1"/>
            <path d="M1.8 8 H14.2 M3 4.8 H13 M3 11.2 H13" stroke="currentColor" stroke-width="1.1"/>
          </svg>
        </li>
      </ul>
    </div>
  </section>
</body>
</html>
```